Health and wellnes company needs business cards

We are a Health and wellness business just relocated to Spain. Here nobody knows our business so we would like to put some of our services on the card. Clean design with logo.

Contact Information for Business Card

Brightmeadow
Clara & Tobias Wennberg
Calle de los Almendros 17
Sanlúcar de Barrameda
Mobile: 0046 731 402768
info@brightmeadow-example.se

Font styles to use
Serif

Colors
85cae6
85acd3
b768aa

Requirements
Must have
• these Services somewhere on the card
• - Private or group yoga
• - Reconnective healing
• - Kitesurfing lessons
• - Massage
• LOgo somewhere
Nice to have
• Colours that go with the logo please

```html
<!DOCTYPE html>
<html lang="en">
<head>
<meta charset="utf-8">
<title>Brightmeadow business card</title>
<link rel="stylesheet" href="https://fonts.googleapis.com/css2?family=Lato:wght@400;700;900&display=swap">
<style>
  :root {
    --backdrop: #2b2b2d;
    --navy: #1d2f5c;
    --navy-deep: #142349;
    --navy-light: #2b4378;
    --ink: #1a1f2e;
    --text-blue: #23407a;
    --teal: #85cae6;
    --paper: #ffffff;
    --paper-shade: #eceef1;
    --rule: #2e4677;
    --icon-fill: #e9edf4;
  }
  * { box-sizing: border-box; margin: 0; padding: 0; }
  html, body { width: 1200px; height: 997px; overflow: hidden; }
  body {
    background: var(--backdrop);
    font-family: "Lato", Arial, sans-serif;
    display: flex; flex-direction: column; align-items: center; justify-content: center; gap: 44px;
  }
  .card {
    width: 760px; height: 434px; border-radius: 30px; position: relative; overflow: hidden;
    box-shadow: 0 14px 34px rgba(0,0,0,.45);
  }

  /* Back side */
  .card-back {
    background: linear-gradient(160deg, var(--navy-light), var(--navy) 45%, var(--navy-deep));
    color: var(--paper);
  }
  .services-title {
    position: absolute; top: 70px; left: 0; right: 0; text-align: center;
    font-weight: 900; font-size: 19px; letter-spacing: 1px;
  }
  .services-title::after {
    content: ""; display: block; width: 44px; height: 2px; background: var(--paper);
    margin: 12px auto 0; opacity: .8;
  }
  .service {
    position: absolute; display: flex; align-items: center; gap: 22px;
    font-size: 20px; letter-spacing: .3px;
  }
  .service-icon {
    width: 62px; height: 62px; border-radius: 50%; flex: none;
    background: var(--icon-fill); border: 3px solid var(--paper);
    box-shadow: 0 0 0 2px rgba(255,255,255,.25);
  }
  .service.left { left: 80px; }
  .service.right { right: 80px; flex-direction: row-reverse; }
  .row-1 { top: 170px; }
  .row-2 { top: 280px; }

  /* Front side */
  .card-front { background: linear-gradient(180deg, var(--paper) 55%, var(--paper-shade)); color: var(--ink); }
  .brand {
    position: absolute; top: 74px; left: 0; right: 0;
    display: flex; flex-direction: column; align-items: center; gap: 18px;
  }
  .brand-mark { width: 70px; height: 70px; border-radius: 50%; background: var(--teal); }
  .brand-name {
    font-weight: 900; font-size: 44px; letter-spacing: 2px; color: var(--navy);
  }
  .people {
    position: absolute; top: 256px; right: 400px; text-align: right;
  }
  .people-names { color: var(--text-blue); font-weight: 700; font-size: 20px; }
  .people-title { font-weight: 700; font-size: 16px; margin-top: 4px; }
  .divider {
    position: absolute; top: 240px; left: 380px; width: 2px; height: 66px; background: var(--rule);
  }
  .contacts {
    position: absolute; top: 236px; left: 404px; list-style: none; font-size: 16px;
  }
  .contacts li { display: flex; align-items: center; gap: 12px; height: 24px; }
  .contacts svg { width: 15px; height: 15px; fill: var(--navy); flex: none; }
  .location-rule {
    position: absolute; top: 343px; left: 30px; right: 30px; height: 1.5px; background: var(--rule);
  }
  .location-label {
    position: absolute; top: 330px; left: 50%; transform: translateX(-50%);
    background: var(--paper-shade); padding: 0 14px;
    color: var(--text-blue); font-weight: 700; font-size: 18px;
  }
  .address {
    position: absolute; top: 362px; left: 0; right: 0; text-align: center; font-size: 17px;
  }
</style>
</head>
<body>

  <section class="card card-back" aria-label="Card back: services">
    <h2 class="services-title">OUR SERVICES</h2>
    <div class="service left row-1"><span class="service-icon" role="img" aria-label="Massage icon"></span>Massage</div>
    <div class="service left row-2"><span class="service-icon" role="img" aria-label="Group yoga icon"></span>Private or group yoga</div>
    <div class="service right row-1"><span class="service-icon" role="img" aria-label="Kitesurfing icon"></span>Kitesurfing lessons</div>
    <div class="service right row-2"><span class="service-icon" role="img" aria-label="Healing hands icon"></span>Reconnective healing</div>
  </section>

  <section class="card card-front" aria-label="Card front: contact details">
    <div class="brand">
      <span class="brand-mark"></span>
      <span class="brand-name">BRIGHTMEADOW</span>
    </div>

    <div class="people">
      <p class="people-names">Clara &amp; Tobias Wennberg</p>
      <p class="people-title">Scientifique des Fusées Financières</p>
    </div>

    <span class="divider"></span>

    <ul class="contacts">
      <li><svg viewBox="0 0 16 16"><path d="M3 1h3l1 4-2 1c1 2 3 4 5 5l1-2 4 1v3c0 1-1 2-2 2C7 15 1 9 1 3c0-1 1-2 2-2z"/></svg>0046 731 402768</li>
      <li><svg viewBox="0 0 16 16"><path d="M1 3h14v10H1z M1 3l7 6 7-6" fill="none" stroke="#1d2f5c" stroke-width="1.6"/></svg>info@brightmeadow-example.se</li>
      <li><svg viewBox="0 0 16 16"><circle cx="8" cy="8" r="6.5" fill="none" stroke="#1d2f5c" stroke-width="1.4"/><path d="M1.5 8h13M8 1.5c-3 3-3 10 0 13M8 1.5c3 3 3 10 0 13" fill="none" stroke="#1d2f5c" stroke-width="1.2"/></svg>www.brightmeadow-example.se</li>
    </ul>

    <span class="location-rule"></span>
    <span class="location-label">Brightmeadow</span>
    <p class="address">Calle de los Almendros 17, Sanlúcar de Barrameda</p>
  </section>

</body>
</html>
```